Marbol Gardens Business Card Design

My company is about Natural products made from Bees Wax, of which I am farming/raising. Products like Honey when in season, body butter, hand cream, lotions, lip balm, soap and more! All Natural, with Beeswax as the base, as it has large healing properties for moisturizing and nourishing your skin.
I would prefer lots of yellows, browns, and blacks (but am open)! I think black ink on the artwork may show up the best. But your the professionals!
The artwork is very dear to me, as my son, Warren did this in the hospital when he was diagnosed with Leukemia, of which he did not survive, at eighteen.
Is it possible to put his initials on this? WJT in light colored ink.
NO BEES, NO US! Oops! I need my name on there. Paula Dimmick and number 555-014-2297. Thank you all so much.

Hospital

Marbol Gardens
All Natural Products
Paula Dimmick
555-014-2297
MarbolGardens@plimmet.com

```html
<!DOCTYPE html>
<html lang="en">
<head>
<meta charset="utf-8">
<title>Marbol Gardens Business Cards</title>
<link rel="stylesheet" href="https://fonts.googleapis.com/css2?family=Open+Sans:wght@300;400;600;800&display=swap">
<style>
  :root {
    --page-bg: #d9d6d2;
    --honey: #f6c90e;
    --band: rgba(247, 201, 40, 0.62);
    --ink: #111111;
    --white: #ffffff;
    --rule: #9b5a1c;
  }
  html, body {
    margin: 0;
    padding: 0;
    width: 1200px;
    height: 1200px;
    overflow: hidden;
    background: var(--page-bg);
    font-family: "Open Sans", Arial, sans-serif;
  }
  .canvas {
    position: relative;
    width: 1200px;
    height: 1200px;
  }
  .card {
    position: absolute;
    overflow: hidden;
  }
  /* Front: son's artwork with initials */
  .card-front {
    left: 80px;
    top: 90px;
    width: 757px;
    height: 466px;
  }
  .artwork {
    position: absolute;
    inset: 0;
    background:
      radial-gradient(circle at 15% 20%, #a8314a 0%, transparent 35%),
      radial-gradient(circle at 85% 15%, #6fb05a 0%, transparent 30%),
      radial-gradient(circle at 90% 85%, #4f9fb0 0%, transparent 30%),
      radial-gradient(circle at 20% 85%, #e77a8e 0%, transparent 35%),
      radial-gradient(circle at 50% 90%, #c9384e 0%, transparent 30%),
      linear-gradient(120deg, #c23a3a 0%, #e8402f 30%, #f08a1e 50%, #f5c224 65%, #8fbf55 100%);
  }
  .initials-band {
    position: absolute;
    left: 0;
    top: 160px;
    width: 100%;
    height: 150px;
    background: var(--band);
  }
  .initials {
    position: absolute;
    left: 0;
    width: 757px;
    text-align: center;
    top: 174px;
    margin: 0;
    color: var(--white);
    font-weight: 600;
    font-size: 66px;
    line-height: 80px;
  }
  .tagline {
    position: absolute;
    left: 0;
    width: 757px;
    text-align: center;
    top: 244px;
    margin: 0;
    color: var(--white);
    font-weight: 300;
    font-size: 34px;
    line-height: 44px;
  }
  /* Back: brand and contact */
  .card-back {
    left: 305px;
    top: 578px;
    width: 758px;
    height: 468px;
    background: var(--honey);
  }
  .brand-name {
    position: absolute;
    left: 0;
    width: 758px;
    text-align: center;
    top: 152px;
    margin: 0;
    color: var(--white);
    font-weight: 800;
    font-size: 62px;
    line-height: 80px;
    padding-left: 10px;
    box-sizing: border-box;
  }
  .brand-tagline {
    position: absolute;
    left: 0;
    width: 758px;
    text-align: center;
    top: 236px;
    margin: 0;
    color: var(--ink);
    font-weight: 400;
    font-size: 37px;
    line-height: 48px;
    letter-spacing: 0.13em;
    padding-left: 12px;
    box-sizing: border-box;
  }
  .brand-rule {
    position: absolute;
    left: 120px;
    top: 296px;
    width: 505px;
    height: 2px;
    background: var(--rule);
  }
  .contact-line {
    position: absolute;
    left: 0;
    width: 758px;
    margin: 0;
    display: flex;
    justify-content: center;
    align-items: center;
    gap: 12px;
    color: var(--ink);
    font-size: 21px;
    line-height: 28px;
    padding-left: 10px;
    box-sizing: border-box;
  }
  .contact-email { top: 323px; }
  .contact-person { top: 361px; }
  .contact-line svg { display: block; }
</style>
</head>
<body>
<main class="canvas">
  <section class="card card-front">
    <div class="artwork" role="img" aria-label="Colourful abstract painting by Warren in reds, oranges, yellows, greens and blues"></div>
    <div class="initials-band"></div>
    <h1 class="initials">WJT</h1>
    <p class="tagline">No bees, No us!</p>
  </section>

  <section class="card card-back">
    <h2 class="brand-name">Marbol Gardens</h2>
    <p class="brand-tagline">NATURAL PRODUCTS</p>
    <div class="brand-rule"></div>
    <p class="contact-line contact-email">
      <svg width="26" height="18" viewBox="0 0 26 18" aria-hidden="true">
        <rect x="0" y="0" width="26" height="18" fill="#111"/>
        <polyline points="1,1 13,10 25,1" fill="none" stroke="#f6c90e" stroke-width="2"/>
        <line x1="1" y1="17" x2="10" y2="8" stroke="#f6c90e" stroke-width="1.5"/>
        <line x1="25" y1="17" x2="16" y2="8" stroke="#f6c90e" stroke-width="1.5"/>
      </svg>
      <span>MarbolGardens@plimmet.com</span>
    </p>
    <p class="contact-line contact-person">
      <span>Paula Dimmick</span>
      <span aria-hidden="true">·</span>
      <span>555-014-2297</span>
    </p>
  </section>
</main>
</body>
</html>
```